Bakery Replacement Lighted Sign Face

We are opening a new bakery that sells only cakes. The name is "The Willow Lantern." We are replacing the current sign face with a new look that states our name and makes a bold statement of fun. We will be known for having 101 cakes that are always ready for immediate pickup or delivery. Our colors are pink, orange, and lime green. An image is provided to see the colors.

Target Market(s)

people who buy cakes for parties and all other occasions

Industry/Entity Type

Cakes

Other font styles liked:
• look at the logo and file for the main font name

Colors
59FF00
82FF00
B8FF75
E3FFCB
F4FFEA
F0912C
F2A743
F7CA91
FBE8D2
FDF5EE
EB3D1F
EC4F4E
F09395
F8D3D4
FCEDEE

Requirements
Must have
• The name of the bakery. Logo can be used as is or changed as shown in one of the uploaded PDFs. Must use either pink, orange, lime green, white, or black. We prefer a bright pink background with white lettering as our first choice, but are willing to be open minded to see all creative concepts. Also the sign is 14 feet long and 42 inches tall so the artwork must fit within those boundaries. Also keep in mind the sign does have a 4 inch black frame. So the graphics area is actually 13 feet 2 inches by 3 feet. Also, in the attached pdf that shows a rough possible layout, the words "101 cakes to go" is on the sign. It is NOT a must. Only use the wording if it adds to your design.
Nice to have
• You are welcome to add additional stars or other fun graphics that could look good.
Should not have
• No images of cakes or other bakery products.

```html
<!DOCTYPE html>
<html lang="en">
<head>
<meta charset="utf-8">
<title>The Willow Lantern – Sign Face</title>
<link rel="stylesheet" href="https://fonts.googleapis.com/css2?family=Comfortaa:wght@700&display=swap">
<style>
  :root {
    --page-bg: #eeeeee;
    --sign-black: #000000;
    --ink-white: #ffffff;
    --brand-pink: #e8619f;
    --brand-orange: #f58e45;
    --brand-lime: #cfe6a4;
  }
  * { margin: 0; padding: 0; box-sizing: border-box; }
  html, body {
    width: 1200px;
    height: 675px;
    overflow: hidden;
    background: var(--page-bg);
  }
  .sign-face {
    position: absolute;
    left: 30px;
    top: 209px;
    width: 1140px;
    height: 257px;
    background: var(--sign-black);
    overflow: hidden;
  }
  .sign-shapes {
    position: absolute;
    inset: 0;
    width: 1140px;
    height: 257px;
  }
  .brand-name {
    position: absolute;
    left: 0;
    right: 0;
    top: 88px;
    text-align: center;
    font-family: "Comfortaa", sans-serif;
    font-weight: 700;
    font-size: 62px;
    line-height: 1;
    letter-spacing: -0.5px;
    color: var(--ink-white);
  }
  .tagline {
    position: absolute;
    right: 22px;
    bottom: 18px;
    font-family: "Comfortaa", sans-serif;
    font-weight: 700;
    font-size: 20px;
    line-height: 1;
    color: var(--ink-white);
  }
</style>
</head>
<body>
  <section class="sign-face">
    <svg class="sign-shapes" viewBox="0 0 1140 257" aria-hidden="true">
      <circle class="accent-dot" cx="44.5" cy="202.5" r="14" fill="var(--brand-pink)"/>
      <circle class="orange-sun" cx="977" cy="-2" r="83" fill="var(--brand-orange)"/>
      <polygon class="lime-star"
        points="1095,32 1100.6,45.4 1115,46.3 1104,55.6 1107.5,69.7 1095,62 1082.5,69.7 1086,55.6 1075,46.3 1089.4,45.4"
        fill="var(--brand-lime)" stroke="var(--brand-lime)" stroke-width="4" stroke-linejoin="round"/>
    </svg>
    <svg class="sign-shapes" viewBox="0 0 1140 257" role="img" aria-label="Lime green striped half-circle decoration">
      <path class="striped-dome" d="M80,257 A81,81 0 0 1 242,257 Z" fill="var(--brand-lime)"/>
    </svg>
    <h1 class="brand-name">The Willow Lantern</h1>
    <p class="tagline">101 cakes to go</p>
  </section>
</body>
</html>
```